Smile club flyer design

I am launching an office smile club and would like a design that sits my branding and that is appealing to customers. I have a design (I need a new one) that has all the information.
My website is maplecrestdentalcarewv.com
Brand color is green. The design can be any color

Target Market(s)

Ages 30+

Industry/Entity Type

Dental

Font styles to use
Serif

Requirements
Must have
• Appealing to patients

```html
<!DOCTYPE html>
<html lang="en">
<head>
<meta charset="utf-8">
<title>Maplecrest Dental Care – Smile Club Membership Flyer</title>
<link href="https://fonts.googleapis.com/css2?family=Libre+Baskerville:wght@700&family=Montserrat:wght@500;600;700;800&family=Poppins:wght@400;500&display=swap" rel="stylesheet">
<style>
  :root{
    --brand-green:#17873f;
    --navy:#0f1e4d;
    --gold:#c8962d;
    --gold-light:#e2b45a;
    --gold-dark:#b5842a;
    --paper:#f1fbfa;
    --ink:#1f2a37;
    --white:#ffffff;
    --stage:#e6ebf0;
  }
  *{box-sizing:border-box;margin:0;padding:0}
  html,body{width:1189px;height:1200px;overflow:hidden}
  body{background:var(--stage);position:relative;font-family:"Poppins",sans-serif}
  .flyer{position:absolute;left:191px;top:30px;width:806px;height:1140px;background:var(--paper);overflow:hidden}

  .brand{position:absolute;top:78px;left:0;width:100%;display:flex;align-items:center;justify-content:center;gap:14px;color:var(--brand-green);font-family:"Montserrat",sans-serif;font-weight:700;font-size:44px;line-height:1}
  .brand-dot{width:18px;height:18px;border-radius:50%;background:var(--brand-green)}

  .intro{position:absolute;top:215px;left:0;width:100%;display:flex;align-items:center;justify-content:center;gap:22px;color:var(--navy)}
  .intro-lead{font-family:"Montserrat",sans-serif;font-weight:700;font-size:27px}
  .club-name{font-family:"Libre Baskerville",serif;font-weight:700;font-size:62px;letter-spacing:2px}

  .membership{position:absolute;top:356px;left:0;width:100%;height:48px}
  .membership::before{content:"";position:absolute;left:0;right:0;top:24px;height:2px;background:var(--gold)}
  .membership-tag{position:absolute;left:240px;width:316px;height:48px;background:var(--gold);border-radius:4px;color:var(--white);font-family:"Montserrat",sans-serif;font-weight:700;font-size:29px;letter-spacing:6px;display:flex;align-items:center;justify-content:center}

  .plans{position:absolute;top:420px;left:9px;width:786px;height:282px;background:var(--navy);padding:10px 11px}
  .plans-title{color:var(--white);font-family:"Montserrat",sans-serif;font-weight:800;font-size:23px;text-align:center;letter-spacing:.3px;margin-bottom:8px}
  .plan-row{display:flex;gap:8px;height:228px}
  .plan{flex:1;background:linear-gradient(135deg,var(--gold-dark),var(--gold-light) 70%,var(--gold));color:var(--white);display:flex;flex-direction:column}
  .plan-head{height:60px;display:flex;flex-direction:column;justify-content:center;text-align:center;font-family:"Montserrat",sans-serif;font-size:18px;line-height:1.15;border-bottom:1px solid rgba(255,255,255,.35)}
  .plan-head b{font-weight:700}
  .plan-head span{font-weight:500}
  .plan-list{list-style:none;flex:1;padding:12px 8px 0 10px;font-size:9.5px;line-height:1.2;position:relative}
  .plan-list li{display:flex;gap:6px;margin-bottom:7px}
  .plan-list svg{flex:none;margin-top:2px}
  .plan-price{height:64px;border-top:1px solid rgba(255,255,255,.35);display:flex;align-items:baseline;justify-content:center;gap:2px;padding-top:6px;font-family:"Montserrat",sans-serif}
  .plan-price strong{font-size:44px;font-weight:600}
  .plan-price small{font-size:13px;font-weight:500}
  .badge-new{position:absolute;right:6px;bottom:8px;width:44px;height:44px;border-radius:50%;background:var(--navy);color:var(--white);font-family:"Montserrat",sans-serif;font-weight:700;font-size:13px;display:flex;align-items:center;justify-content:center}

  .family-photo{position:absolute;top:728px;left:0;width:100%;height:317px;background:linear-gradient(90deg,#cfdde8,#e8eef3 40%,#dde8ef 70%,#c9d9e5)}

  .footer{position:absolute;top:1045px;left:0;width:100%;height:95px;background:var(--white);display:flex;align-items:center;padding:0 24px 0 62px}
  .join-title{font-family:"Montserrat",sans-serif;font-weight:700;font-size:23px;color:var(--ink);letter-spacing:.5px}
  .join-phone{display:flex;align-items:center;gap:4px;font-family:"Montserrat",sans-serif;font-weight:800;font-size:34px;color:var(--gold);line-height:1.1}
  .divider{width:1px;height:56px;background:#9aa3ad;margin:0 16px}
  .finance-title{font-family:"Montserrat",sans-serif;font-weight:700;font-size:13px;color:var(--ink);letter-spacing:.5px}
  .finance-partners{display:flex;gap:20px;margin:6px 0 5px;align-items:center}
  .partner{display:flex;align-items:center;gap:6px;font-family:"Montserrat",sans-serif;font-weight:700;font-size:20px;color:var(--ink)}
  .partner i{width:12px;height:12px;border-radius:50%;background:var(--gold);display:block}
  .finance-note{font-size:7.5px;font-weight:500;color:var(--ink)}
</style>
</head>
<body>
<main class="flyer">
  <header class="brand">
    <span class="brand-dot"></span>
    <span class="brand-name">Maplecrest Dental Care</span>
  </header>

  <section class="intro">
    <span class="intro-lead">INTRODUCING</span>
    <span class="club-name">Smile Club</span>
  </section>

  <div class="membership"><div class="membership-tag">MEMBERSHIP</div></div>

  <section class="plans">
    <h2 class="plans-title">AFFORDABLE DENTAL CARE NO INSURANCE REQUIRED</h2>
    <div class="plan-row">
      <article class="plan">
        <div class="plan-head"><b>CORE CARE</b><span>PREVENTIVE</span></div>
        <ul class="plan-list">
          <li><svg width="7" height="7" viewBox="0 0 10 10"><path d="M1 5l3 3 5-7" fill="none" stroke="#fff" stroke-width="1.6"/></svg>Comprehensive Annual Exam</li>
          <li><svg width="7" height="7" viewBox="0 0 10 10"><path d="M1 5l3 3 5-7" fill="none" stroke="#fff" stroke-width="1.6"/></svg>2 Professional Cleanings per Year</li>
          <li><svg width="7" height="7" viewBox="0 0 10 10"><path d="M1 5l3 3 5-7" fill="none" stroke="#fff" stroke-width="1.6"/></svg>Routine Bitewing X-rays</li>
          <li><svg width="7" height="7" viewBox="0 0 10 10"><path d="M1 5l3 3 5-7" fill="none" stroke="#fff" stroke-width="1.6"/></svg>10% Savings on Treatment</li>
        </ul>
        <div class="plan-price"><strong>$39</strong><small>/MONTH</small></div>
      </article>
      <article class="plan">
        <div class="plan-head"><b>BRIGHT</b><span>COSMETIC</span></div>
        <ul class="plan-list">
          <li><svg width="7" height="7" viewBox="0 0 10 10"><path d="M1 5l3 3 5-7" fill="none" stroke="#fff" stroke-width="1.6"/></svg>Annual In-Office Whitening (Top &amp; Bottom)</li>
          <li><svg width="7" height="7" viewBox="0 0 10 10"><path d="M1 5l3 3 5-7" fill="none" stroke="#fff" stroke-width="1.6"/></svg>Custom Whitening Trays</li>
          <li><svg width="7" height="7" viewBox="0 0 10 10"><path d="M1 5l3 3 5-7" fill="none" stroke="#fff" stroke-width="1.6"/></svg>15% Savings on Elective Treatment</li>
        </ul>
        <div class="plan-price"><strong>$59</strong><small>/MONTH</small></div>
      </article>
      <article class="plan">
        <div class="plan-head"><b>TOTAL SMILE</b><span>PERIODONTAL</span></div>
        <ul class="plan-list">
          <li><svg width="7" height="7" viewBox="0 0 10 10"><path d="M1 5l3 3 5-7" fill="none" stroke="#fff" stroke-width="1.6"/></svg>3-4 Perio Maintenance Visits per Year</li>
          <li><svg width="7" height="7" viewBox="0 0 10 10"><path d="M1 5l3 3 5-7" fill="none" stroke="#fff" stroke-width="1.6"/></svg>1 Comprehensive Exam</li>
          <li><svg width="7" height="7" viewBox="0 0 10 10"><path d="M1 5l3 3 5-7" fill="none" stroke="#fff" stroke-width="1.6"/></svg>Diagnostic X-rays</li>
          <li><svg width="7" height="7" viewBox="0 0 10 10"><path d="M1 5l3 3 5-7" fill="none" stroke="#fff" stroke-width="1.6"/></svg>15% Savings on Restorative &amp; Elective Care</li>
        </ul>
        <div class="plan-price"><strong>$89</strong><small>/MONTH</small></div>
      </article>
      <article class="plan">
        <div class="plan-head"><b>SMILE REFRESH</b><span>PACKAGE</span></div>
        <ul class="plan-list">
          <li><svg width="7" height="7" viewBox="0 0 10 10"><path d="M1 5l3 3 5-7" fill="none" stroke="#fff" stroke-width="1.6"/></svg>Cleaning + Comprehensive Exam + Whitening</li>
          <li><svg width="7" height="7" viewBox="0 0 10 10"><path d="M1 5l3 3 5-7" fill="none" stroke="#fff" stroke-width="1.6"/></svg><b>Limited Time Offer</b></li>
          <li class="badge-new">New</li>
        </ul>
        <div class="plan-price"><strong>$499</strong><small>/MONTH</small></div>
      </article>
    </div>
  </section>

  <div class="family-photo" role="img" aria-label="Smiling family of four with a dentist in a bright dental office"></div>

  <footer class="footer">
    <div class="join">
      <div class="join-title">JOIN SMILE CLUB TODAY!</div>
      <div class="join-phone">
        <svg width="26" height="26" viewBox="0 0 24 24"><circle cx="12" cy="12" r="12" fill="var(--gold)"/><path d="M8.5 6.5l2 2-1.2 1.6a7 7 0 0 0 4.6 4.6l1.6-1.2 2 2-1.5 1.8c-4.3-.2-8.6-4.5-8.8-8.8z" fill="#fff"/></svg>
        304-555-0182
      </div>
    </div>
    <div class="divider"></div>
    <div class="finance">
      <div class="finance-title">FLEXIBLE FINANCING FOR TREATMENT :</div>
      <div class="finance-partners">
        <span class="partner"><i></i>PayEase</span>
        <span class="partner">Plumline</span>
      </div>
      <div class="finance-note">PAYMENT PLANS AVAILABLE | *$49 Lifetime Activation Fee (Non-Refundable)</div>
    </div>
  </footer>
</main>
</body>
</html>
```